Online Advice via Video Site requires Cutting Edge Homepage

We need a creative new and exciting webdesign for our tutoring via video-chat website.

We have prepared a "demo" homepage for you to see various promotional material that we think would be suitable for the homepage. http://www.quizlanterna.com/demo

The actual site is undergoing some final tinkering but can be accessed and used at http://www.quizlanterna.com

There is NO NEED to take any colours or design structure from this.

We expect the logo to be changed to match the new site. The new logo should match the site's function.

I have included some other projects that we like the look of:
http://www.artflockly.com.au/design/143762
http://www.artflockly.com.au/design/561630
http://www.artflockly.com.au/design/247199
http://www.artflockly.com.au/design/255195
http://www.bravolumo.tv/

Target Market(s)

People that will work as tutors/advisers or be student/clients

Industry/Entity Type

Tutoring

Requirements
Must have
• The search is the main feature of the homepage

After the search the next goal of the page is to get people to sign up to the site

Login, (optional inclusion of the chatterbox login - if you don't include it then you need only have a "login" button... no username or password input fields)

Footer
Nice to have
• The promotional material for the site, the colours on the Slidora file CAN BE changed to suit the new design you propose.

```html
<!DOCTYPE html>
<html lang="en">
<head>
<meta charset="utf-8">
<title>Quiz Lanterna – Online Advice via Video</title>
<link href="https://fonts.googleapis.com/css2?family=Arimo:wght@400;700&display=swap" rel="stylesheet">
<style>
:root{
  --blue:#1f4fc9;
  --blue-dark:#0a35a8;
  --blue-light:#5aa3ee;
  --ink:#333;
  --ink-soft:#555;
  --ink-muted:#777;
  --panel:#ebebeb;
  --footer:#cdcdcd;
  --field:#c8c8c8;
  --white:#fff;
}
*{box-sizing:border-box;margin:0;padding:0}
html,body{width:1000px;height:1200px;overflow:hidden}
body{position:relative;background:var(--white);font-family:"Arimo",Arial,sans-serif;color:var(--ink)}
.abs{position:absolute}

.site-header{left:0;top:0;width:1000px;height:115px;background:linear-gradient(#fff 60%,#f1f1f1);border-bottom:1px solid #e2e2e2}
.brand{left:40px;top:40px;font-size:30px;font-weight:400;color:var(--ink-soft);letter-spacing:-.5px}
.phone{left:376px;top:45px;font-size:24px;font-weight:700;color:var(--blue)}
.signup-btn{left:705px;top:31px;width:96px;height:52px;border-radius:5px;background:linear-gradient(#fff,#e3e3e3);box-shadow:0 2px 3px rgba(0,0,0,.3);text-align:center;color:var(--blue);font-weight:700;line-height:1}
.signup-btn .big{display:block;font-size:24px;margin-top:5px}
.signup-btn .small{display:block;font-size:14px;margin-top:1px;padding-left:36px}
.login-field{left:838px;width:119px;height:24px;background:var(--field);color:#777;font-size:11px;padding:7px 4px}
.remember{left:838px;top:88px;font-size:10px;color:#666;display:flex;align-items:center;gap:4px}
.remember i{display:block;width:10px;height:10px;background:#ddd;border:1px solid #bbb}
.go-btn{left:926px;top:85px;width:31px;height:20px;background:var(--blue);color:#fff;font-size:10px;font-weight:700;text-align:center;line-height:20px}

.main-nav{left:29px;top:125px;width:932px;height:32px;border-radius:3px;background:linear-gradient(#2a5fdc,var(--blue-dark));display:flex;align-items:center;justify-content:space-around;padding:0 14px;color:#fff;font-size:11px;font-weight:700}

.hero{left:31px;top:169px;width:930px;height:261px;border:1px solid #ccc;background:linear-gradient(90deg,#f6f6f6,#eaeaea 55%,#f2f2f2);overflow:hidden}
.hero-photo{position:absolute;right:0;top:0;width:400px;height:259px;background:linear-gradient(90deg,rgba(234,234,234,0),#d9d4cf 30%,#c8b9ae 60%,#e9e6e2)}
.hero-text{position:absolute;left:19px;top:37px;font-size:24.2px;line-height:29px;color:var(--blue)}
.hero-cta{position:absolute;left:19px;top:163px;font-size:29px;color:var(--blue)}

.search-panel{left:109px;top:401px;width:780px;height:77px;border-radius:8px;border:1px solid #1d60c9;background:linear-gradient(var(--blue-light),#2d7de0)}
.search-input{position:absolute;left:16px;top:14px;width:539px;height:46px;border-radius:3px;background:linear-gradient(#fff,#e2e2e2);font-size:12px;padding:17px 8px;color:#222}
.search-btn{position:absolute;left:572px;top:12px;width:187px;height:52px;border-radius:8px;background:#333;color:#fff;font-size:18px;display:flex;align-items:center;padding-left:12px;gap:12px}

.features{left:31px;top:493px;width:930px;height:428px;background:radial-gradient(ellipse at 50% 35%,#fafafa,var(--panel) 70%)}
.card{position:absolute;border-radius:8px;background:linear-gradient(#fff,#e0e0e0);box-shadow:0 1px 4px rgba(0,0,0,.25)}
.card-icon{position:absolute;left:8px;top:14px;width:50px;height:62px;border-radius:4px;background:linear-gradient(#6b8cc7,#2e4f95)}
.card-title{position:absolute;left:62px;top:15px;font-size:12px;font-weight:700;color:var(--ink);white-space:nowrap}
.card-text{position:absolute;left:62px;top:35px;font-size:12px;line-height:14.5px;color:#444;white-space:nowrap}
.pay-marks{position:absolute;left:4px;top:22px;display:grid;grid-template-columns:22px 22px;gap:4px 4px}
.pay-marks i{display:block;width:22px;height:13px;border-radius:2px;background:#fff;border:1px solid #bbb}
.about{position:absolute;left:13px;top:24px;width:310px;font-size:12px;font-weight:700;line-height:14.5px;color:#444}
.about-item{margin-bottom:14px;white-space:nowrap}
.topics-divider{position:absolute;left:336px;top:6px;width:1px;height:190px;background:#999}
.topics{position:absolute;left:377px;top:21px;font-size:12px;font-weight:700;color:#444;white-space:nowrap}
.topics-title{font-size:12px;font-weight:700;color:var(--ink);margin-bottom:15px}
.topic{list-style:none;margin-bottom:10px}

.site-footer{left:0;top:940px;width:1000px;height:260px;background:var(--footer)}
.foot-col{position:absolute;top:28px}
.foot-col h4{font-size:14px;font-weight:700;color:var(--ink-soft);margin-bottom:23px}
.foot-col li{list-style:none;font-size:11px;font-weight:700;color:var(--ink-muted);margin-bottom:11.5px}
.news-label{left:694px;font-size:11px;font-weight:700;color:var(--ink-muted)}
.news-field{left:734px;width:204px;height:24px;border-radius:12px;background:#999}
.submit-btn{left:843px;top:1096px;width:95px;height:24px;border-radius:4px;background:linear-gradient(var(--blue-light),#1d60c9);color:#fff;font-size:12px;font-weight:700;text-align:center;line-height:24px}
.legal{left:24px;top:1169px;font-size:11px;font-weight:700;color:#222}
.legal a{color:var(--blue);font-style:italic;font-weight:400;text-decoration:none}
.social{left:597px;top:1159px;display:flex;gap:10px}
.social i{display:block;width:26px;height:26px;border-radius:4px;background:linear-gradient(#bbb,#8a8a8a)}
</style>
</head>
<body>

<header class="abs site-header"></header>
<div class="abs brand">Quiz Lanterna</div>
<div class="abs phone">+ 1800 555 0199</div>
<div class="abs signup-btn"><span class="big">Signup</span><span class="small">here</span></div>
<div class="abs login-field" style="top:20px">Name</div>
<div class="abs login-field" style="top:51px">Password</div>
<div class="abs remember"><i></i>Remember me</div>
<div class="abs go-btn">Go</div>

<nav class="abs main-nav">
  <span>HOME</span><span>|</span><span>STUDENT</span><span>|</span><span>ADVISORS</span><span>|</span><span>TOPICS</span><span>|</span><span>BLOG</span><span>|</span><span>FAQS</span><span>|</span><span>SITEMAP</span><span>|</span><span>ABOUT US</span><span>|</span><span>OUR TECHNOLOGY</span><span>|</span><span>CONTACT</span>
</nav>

<section class="abs hero">
  <div class="hero-photo" role="img" aria-label="Photo of a smiling businesswoman holding a phone in a bright office"></div>
  <div class="hero-text">IMAGINE IF, WHENEVER YOU HAD A<br>PROBLEM YOU COULD INSTANTLY ACCESS<br>THE WORLD'S EXPERTS TO SOLVE IT.</div>
  <div class="hero-cta">NOW YOU CAN!</div>
</section>

<div class="abs search-panel">
  <div class="search-input">SEARCH TERMS</div>
  <div class="search-btn">
    <svg width="36" height="40" viewBox="0 0 36 40" aria-hidden="true"><circle cx="14" cy="14" r="11" fill="#2d6fd6" stroke="#ccc" stroke-width="3"/><line x1="22" y1="22" x2="33" y2="37" stroke="#999" stroke-width="5" stroke-linecap="round"/></svg>
    SEARCH
  </div>
</div>

<section class="abs features">
  <div class="card" style="left:24px;top:30px;width:252px;height:132px">
    <div class="card-icon" role="img" aria-label="Illustration of an advisor in a suit"></div>
    <div class="card-title">INSTANT PERSONAL ADVICE</div>
    <div class="card-text">Find advisors<br>waiting online<br><br>OR<br><br>Book appointment when it suits</div>
  </div>
  <div class="card" style="left:334px;top:30px;width:252px;height:132px">
    <div class="card-icon" style="width:60px;height:66px" role="img" aria-label="Illustration of a video call on a monitor with webcam"></div>
    <div class="card-title" style="left:74px">DIRECT VIDEO CONFERENCE</div>
    <div class="card-text" style="left:91px;top:43px">Video in "x" quality<br>Messaging features</div>
  </div>
  <div class="card" style="left:655px;top:30px;width:252px;height:132px">
    <div class="card-icon" style="width:44px;height:54px" role="img" aria-label="Illustration of a profile folder"></div>
    <div class="card-title">ADVISORS AND/OR CLIENTS</div>
    <div class="card-text" style="top:43px">Advisors - Enter your:<br>Topic, buget, availability<br>Clients - SEARCH now<br>Compare ratea, rating &amp; resumes</div>
  </div>
  <div class="card" style="left:24px;top:201px;width:252px;height:132px">
    <div class="pay-marks" aria-label="Accepted payment methods"><i></i><i></i><i></i><i></i><i></i><i></i></div>
    <div class="card-title" style="left:69px;top:19px">PAYLIO OR CREDIT CARD</div>
    <div class="card-text" style="left:69px;top:42px">Charges based on individual<br>advisor's rate<br>Pay only for the time you use<br>Pay via paylio or credit card<br>Be paid via credit card</div>
  </div>
  <div class="card" style="left:325px;top:201px;width:592px;height:202px">
    <div class="about">
      <div class="about-item">QuizLanterna is the place for e-learning,<br>mentoring &amp; professional advice</div>
      <div class="about-item">It instantly connects people with knowledge and<br>those who need it</div>
      <div class="about-item">Connects people for ongoing advice or on off<br>answers</div>
      <div class="about-item">Ask questions and/or work exactly when it suits<br>you</div>
    </div>
    <div class="topics-divider"></div>
    <div class="topics">
      <div class="topics-title">ADVISORS BY TOPICS</div>
      <ul><li class="topic">English</li><li class="topic">Building</li><li class="topic">Cultural Studies</li><li class="topic">Criminology</li><li class="topic">Agriculture</li><li class="topic">Veterinary Science</li></ul>
    </div>
  </div>
</section>

<footer class="abs site-footer">
  <div class="foot-col" style="left:40px"><h4>ABOUT US</h4><ul><li>Company Info</li><li>Services</li><li>Clients</li></ul></div>
  <div class="foot-col" style="left:211px"><h4>ADVICE</h4><ul><li>FAQ</li><li>Solutions</li><li>Contacts</li></ul></div>
  <div class="foot-col" style="left:372px"><h4>JOIN IN</h4><ul><li>Sign Up</li><li>Forums</li><li>Promotions</li></ul></div>
  <div class="foot-col" style="left:523px"><h4>DOWNLOADS</h4><ul><li>Press Releases</li><li>Banners &amp; Logos</li><li>Podcasts</li></ul></div>
  <div class="foot-col" style="left:694px"><h4>NEWLETTER SIGNUP</h4></div>
</footer>
<div class="abs news-label" style="top:1009px">Name</div>
<div class="abs news-field" style="top:1003px"></div>
<div class="abs news-label" style="top:1057px">Email</div>
<div class="abs news-field" style="top:1048px"></div>
<div class="abs submit-btn">SUBMIT</div>
<div class="abs legal">© 2012 quizlanterna.com &nbsp;| &nbsp;<a>Privacy Policy</a> &nbsp;| &nbsp;<a>Terms &amp; Conditions</a></div>
<div class="abs social" aria-label="Social sharing links"><i></i><i></i><i></i><i></i><i></i><i></i><i></i><i></i><i></i><i></i><i></i></div>

</body>
</html>
```